Book cover "Beyond the quiet"

Creation of a cover with three submitted images The book is an autobiography of a man who stayed three years hided in an attic with his parents to escape from the Germans soldiers during the II World War. Author: Tomas Veldrin Title: Beyond the quiet SubTitle (not very important): Tomas et l% 26 # 39; ing% 26 # 233; nieur Publishers (with Gill sans Light Font): Editions Marvolt 16 x 24 cm
Updates

Besoin de quelques jours pour choisir un design

Besoin de plus de jours pour examiner

Target Market(s)

General public (adults)

Colors

Designer to choose colors to be used in the design.

Requirements
Must have
• The three joined images

```html
<!DOCTYPE html>
<html lang="en">
<head>
<meta charset="utf-8">
<title>Beyond the quiet — Book Cover</title>
<link rel="stylesheet" href="https://fonts.googleapis.com/css2?family=Allerta+Stencil&family=Lato:wght@300&display=swap">
<style>
  :root {
    --page-bg: #3f4557;
    --cover-black: #0b0b0b;
    --cover-shade: #1d1d1d;
    --ring-dark: #141414;
    --ring-edge: #2a2a2a;
    --scope-light: #6fb35a;
    --scope-mid: #3c7a2e;
    --scope-deep: #17380f;
    --title-white: #f2f2f2;
    --label-ink: #0e0e0e;
    --author-grey: #e6e6e6;
  }
  html, body {
    margin: 0;
    width: 1200px;
    height: 900px;
    overflow: hidden;
    background: var(--page-bg);
  }
  .cover {
    position: absolute;
    left: 320px;
    top: 42px;
    width: 560px;
    height: 816px;
    background: var(--cover-black);
    overflow: hidden;
  }
  .cover__street-photo {
    position: absolute;
    inset: 0;
    background:
      linear-gradient(180deg, rgba(11,11,11,0.9) 0%, rgba(11,11,11,0.4) 35%, rgba(11,11,11,0.55) 70%, rgba(11,11,11,0.85) 100%),
      linear-gradient(100deg, var(--cover-shade) 0%, #121212 45%, #232323 75%, #151515 100%);
  }
  .scope {
    position: absolute;
    left: 99px;
    top: 5px;
    width: 368px;
    height: 368px;
    border-radius: 50%;
    background: radial-gradient(circle at 50% 45%, var(--ring-edge) 0%, var(--ring-dark) 70%, #000 100%);
    box-shadow: 0 4px 14px rgba(0,0,0,0.7);
  }
  .scope__view {
    position: absolute;
    left: 20px;
    top: 20px;
    width: 328px;
    height: 328px;
    border-radius: 50%;
    background: radial-gradient(circle at 60% 40%, var(--scope-light) 0%, var(--scope-mid) 45%, var(--scope-deep) 100%);
    box-shadow: inset 0 0 18px rgba(0,0,0,0.8);
  }
  .title {
    position: absolute;
    left: 0;
    right: 0;
    top: 500px;
    text-align: center;
    font-family: "Allerta Stencil", sans-serif;
    text-transform: uppercase;
  }
  .title__main {
    display: block;
    font-size: 58px;
    line-height: 1;
    letter-spacing: 0.32em;
    margin-right: -0.32em;
    color: var(--title-white);
  }
  .title__tags {
    display: flex;
    justify-content: center;
    gap: 46px;
    margin-top: 20px;
  }
  .title__tag {
    background: var(--title-white);
    color: var(--label-ink);
    font-size: 40px;
    line-height: 1;
    letter-spacing: 0.3em;
    padding: 3px 0 3px 10px;
  }
  .author {
    position: absolute;
    left: 0;
    right: 0;
    top: 712px;
    text-align: center;
    font-family: "Lato", sans-serif;
    font-weight: 300;
    font-size: 42px;
    color: var(--author-grey);
    margin: 0;
  }
</style>
</head>
<body>
  <main class="cover">
    <div class="cover__street-photo" role="img" aria-label="Faded black and white photograph of an old city street with tall buildings"></div>
    <div class="scope">
      <div class="scope__view" role="img" aria-label="Green night-vision photograph of a wooden attic beside a portrait of a young man in a suit and tie"></div>
    </div>
    <h1 class="title">
      <span class="title__main">Beyond</span>
      <span class="title__tags">
        <span class="title__tag">The</span>
        <span class="title__tag">Quiet</span>
      </span>
    </h1>
    <p class="author">Tomas Veldrin</p>
  </main>
</body>
</html>
```